HiItsJonBrell.com needs a modern, eye-catching business card design

My name is Jon Brell and I own a video training (software development industry) website. I need a business card design that is eye catching for when I travel to conferences or do seminars. I would prefer something simple but bold. Something along the lines of this: https://pixvaultstatic.example/gallery_img/530172/44018/44018_9917302_530172_image.jpg

Note that I do not have a specific logo, but I do have an caricature I use on my site of myself. I've not attached it because I'm not really a fan of having it on my business cards. I would prefer lettering instead of an image. You can go to my website (https://hiitsjonbrell.com) for inspiration.

I want to add the following information on my card (the order of these, their size, and their casing is up to you):

Jon Brell
jon@HiItsJonBrell.com
@HiItsJonBrell
HiItsJonBrell.com
vidsharehub.example/HiItsJonBrell

I would also like to have somewhere on the card a small ad that says "Get a free course at https://HiItsJonBrell.com/FreeCourse". Feel free to play with that wording or layout if you need. I would prefer this text to be at the bottom of the card and subtle. Some small eye-catching thing might be ok but nothing huge or garish.

I plan on printing this card at pressquill.example (https://www.pressquill.example/us/design-guidelines/business-cards.html). I would like it to be the standard size (3.66" x 2.16"). I would prefer rounded corners and horizontal orientation. This is a two-side design. I would prefer the side with all of the information be primarily white but I like color text (again, flexible on that). On the front side, I like simple. Maybe just HiItsJonBrell.com (casing on that is up to you - whatever looks and reads the best - that goes for all of the casing). As for font choices, I prefer a modern, clean font. For example, Open Sans Light can be a nice option.

Website Info (might be helpful for the card):
Color Palette

Darkest blue - #263246
Alternate blue - #2F4E6A
Light blue - #2A98C3
Orange - #FF6201
White - #FFFFFF

Font for Jon Brell Logo

Jellyka Estryas Handwriting
http://www.typecrate.example/jellyka_estryas_handwriting.font

Fonts for Site Content and VidShare Thumbnails

Lovelo (bold title font)
http://www.glyphmill.example/lovelo-font/

Open Sans (body font)
http://www.letterbarn.example/fonts/open-sans

Industry/Entity Type

Software Development

Contact Information for Business Card

Jon Brell
jon@HiItsJonBrell.com
@HiItsJonBrell
HiItsJonBrell.com
vidsharehub.example/HiItsJonBrell

Get a free course at https://HiItsJonBrell.com/FreeCourse

Colors

Designer to choose colors to be used in the design.

Requirements
Nice to have
• Modern color - maybe primarily a color on the front and then that color as an accent on the back.
Should not have
• Lots of colors - I LOVE color but do not want a rainbow of colors on the card.

```html
<!DOCTYPE html>
<html lang="en">
<head>
<meta charset="utf-8">
<title>HiItsJonBrell.com Business Card</title>
<link href="https://fonts.googleapis.com/css2?family=Questrial&family=Saira:wght@500&display=swap" rel="stylesheet">
<style>
  :root {
    --backdrop: #b9bec2;
    --brick: #a23a2c;
    --brick-line: #b85a44;
    --paper: #ecf2ee;
    --green: #76b943;
    --orange: #f4b06a;
    --blue: #2a98c3;
    --grey-text: #6f6f6f;
    --circuit-light: #dfe7e2;
  }
  * { margin: 0; padding: 0; box-sizing: border-box; }
  html, body { width: 1200px; height: 1200px; overflow: hidden; }
  body { background: var(--backdrop); position: relative; font-family: "Questrial", sans-serif; }

  .card {
    position: absolute; left: 270px; width: 667px; height: 394px;
    border-radius: 18px; overflow: hidden;
  }
  .card-front { top: 154px; background: var(--brick); }
  .card-back { top: 677px; background: var(--paper); }

  .circuit-front {
    position: absolute; left: 0; top: 0; width: 260px; height: 100%;
    background: linear-gradient(90deg, rgba(200,100,75,0.45), rgba(162,58,44,0));
  }
  .circuit-back {
    position: absolute; right: 0; top: 0; width: 180px; height: 100%;
    background: linear-gradient(270deg, var(--circuit-light), rgba(236,242,238,0));
  }
  .corner { position: absolute; }
  .corner-front { left: 0; bottom: 0; }
  .corner-back { right: 0; bottom: 0; }

  .front-domain {
    position: absolute; left: 286px; top: 166px;
    font-family: "Saira", sans-serif; font-weight: 500; font-size: 30px;
    font-variant: small-caps; letter-spacing: 1.5px; color: #fff;
  }

  .identity { position: absolute; right: 371px; top: 136px; text-align: right; color: var(--green); }
  .identity-name { font-size: 27px; line-height: 1; letter-spacing: 0.5px; }
  .identity-role { font-size: 14.5px; margin-top: 2px; }

  .divider { position: absolute; left: 315px; top: 107px; }

  .contacts { position: absolute; left: 334px; top: 118px; list-style: none; color: var(--green); font-size: 15px; }
  .contacts li { height: 23.4px; display: flex; align-items: center; }
  .contacts .icon { width: 12px; height: 12px; margin-right: 6px; flex: none; }
  .contacts .no-icon { padding-left: 34px; }

  .promo-lead {
    position: absolute; left: 180px; top: 318px;
    font-size: 14px; font-variant: small-caps; letter-spacing: 1.5px; color: var(--orange);
  }
  .promo-lead .at { color: var(--grey-text); }
  .promo-url {
    position: absolute; left: 232px; top: 333px;
    font-size: 14px; font-variant: small-caps; letter-spacing: 1.2px; color: var(--blue);
  }
</style>
</head>
<body>

<section class="card card-front">
  <div class="circuit-front" role="img" aria-label="Faint circuit-board trace pattern"></div>
  <svg class="corner corner-front" width="40" height="40" viewBox="0 0 40 40">
    <polygon points="0,8 32,40 26,40 0,14" fill="var(--green)"/>
  </svg>
  <p class="front-domain">HiItsJonBrell.com</p>
</section>

<section class="card card-back">
  <div class="circuit-back" role="img" aria-label="Light circuit-board trace pattern"></div>
  <svg class="corner corner-back" width="44" height="44" viewBox="0 0 44 44">
    <polygon points="44,2 44,12 14,44 4,44" fill="var(--brick)"/>
  </svg>

  <div class="identity">
    <h1 class="identity-name" style="font-weight:400">JON BRELL</h1>
    <p class="identity-role">Programmer &amp; Instructor</p>
  </div>

  <svg class="divider" width="10" height="128" viewBox="0 0 10 128">
    <line x1="5" y1="0" x2="5" y2="128" stroke="var(--brick)" stroke-width="1"/>
    <circle cx="5" cy="59" r="3.5" fill="var(--paper)" stroke="var(--brick)" stroke-width="1"/>
  </svg>

  <ul class="contacts">
    <li>
      <svg class="icon" viewBox="0 0 12 12"><rect x="0.5" y="0.5" width="11" height="11" fill="none" stroke="var(--brick)"/><rect x="2.5" y="3" width="7" height="6" fill="var(--brick)"/></svg>
      jon@HiItsJonBrell.com
    </li>
    <li class="no-icon">@HiItsJonBrell</li>
    <li>
      <svg class="icon" viewBox="0 0 12 12"><rect x="0.5" y="0.5" width="11" height="11" fill="none" stroke="var(--brick)"/><circle cx="6" cy="6" r="3.5" fill="none" stroke="var(--brick)" stroke-width="0.8"/><line x1="2.5" y1="6" x2="9.5" y2="6" stroke="var(--brick)" stroke-width="0.8"/><line x1="6" y1="2.5" x2="6" y2="9.5" stroke="var(--brick)" stroke-width="0.8"/></svg>
      HiItsJonBrell.com
    </li>
    <li>
      <svg class="icon" viewBox="0 0 12 12"><rect x="0.5" y="0.5" width="11" height="11" fill="none" stroke="var(--brick)"/><rect x="2.5" y="3.5" width="7" height="5" fill="var(--brick)"/></svg>
      vidsharehub.example/HiItsJonBrell
    </li>
  </ul>

  <p class="promo-lead">Get a free course <span class="at">AT</span></p>
  <p class="promo-url">HiItsJonBrell.com/FreeCourse</p>
</section>

</body>
</html>
```